Pebble and Pine App design

I need a full app design, colours, images, fonts, and a mock up design of the app to bring to the developer.

Pebble and Pine is a free app that allows cafes, independent cafe and chains of cafes to let their customers know what the soup of the day and what specials they have on that day through the app. Each cafe will have a profile which they can upload the Pebble and Pine daily.

The user home screen will include google maps showing their location with the registered cafes and eateries around them. including a list of the cafe and distances below. as seen in attachment.

Target Market(s)

Cafes , anyone who enjoys eating soups and off local cafe specials boards

Requirements
Must have
• I would like a complete app design based on the attached images.

```html
<!DOCTYPE html>
<html lang="en">
<head>
<meta charset="utf-8">
<title>Pebble and Pine App Screens</title>
<link href="https://fonts.googleapis.com/css2?family=Lato:wght@400;700;900&display=swap" rel="stylesheet">
<style>
  :root{
    --page:#fff8ea;
    --amber:#f9b52c;
    --amber-text:#f6ae2b;
    --cream-yellow:#fcdb8e;
    --soft-yellow:#fde3a4;
    --splash-grey:#eeeeee;
    --paper:#f6f4f1;
    --white:#ffffff;
    --ink:#555555;
    --muted:#8a8a8a;
    --social:#3a5a9c;
  }
  *{box-sizing:border-box;margin:0;padding:0}
  html,body{width:1200px;height:596px;overflow:hidden}
  body{background:var(--page);font-family:"Lato",sans-serif;position:relative}
  .screen{position:absolute;top:141px;width:131px;height:283px;overflow:hidden;box-shadow:0 1px 3px rgba(0,0,0,.12)}
  .screen--splash-light{left:65px;background:var(--splash-grey)}
  .screen--splash-yellow{left:272px;background:radial-gradient(circle at 50% 48%,#fde7a8 0%,#fbd677 60%,#f6cc6a 100%)}
  .screen--cafe-light{left:458px;background:var(--paper)}
  .screen--cafe-yellow{left:643px;background:var(--cream-yellow)}
  .screen--user-light{left:829px;background:var(--white)}
  .screen--user-yellow{left:1015px;background:var(--soft-yellow)}

  .brand-badge{position:absolute;left:20px;top:67px;width:91px;height:91px;border-radius:50%;background:var(--white);border:3px solid var(--amber);display:flex;align-items:center;justify-content:center;text-align:center}
  .brand-badge__name{font-weight:900;color:var(--amber-text);font-size:12px;line-height:1.15;text-transform:uppercase;letter-spacing:.3px}

  .mini-badge{position:absolute;left:8px;top:7px;width:23px;height:23px;border-radius:50%;background:var(--white);border:1.2px solid var(--amber);display:flex;align-items:center;justify-content:center;text-align:center;z-index:2}
  .mini-badge__name{font-weight:900;color:var(--amber-text);font-size:3.4px;line-height:1.15;text-transform:uppercase}

  .photo-top{position:absolute;left:0;top:0;width:131px;height:92px}
  .photo-bottom{position:absolute;left:0;bottom:0;width:131px}

  .title{position:absolute;left:0;width:131px;top:94px;text-align:center;font-weight:900;font-size:8.4px;letter-spacing:.2px;color:var(--amber-text)}
  .title--light{color:var(--white)}

  .field{position:absolute;left:19px;width:95px;height:15px;background:var(--white);display:flex;align-items:center;justify-content:space-between;padding:0 5px;font-size:4.8px;color:var(--ink)}
  .field--tall{height:22px;align-items:flex-start;padding-top:5px}
  .field svg{width:5px;height:5px}

  .button{position:absolute;left:19px;width:95px;height:15px;background:var(--amber);color:var(--white);font-size:5.6px;font-weight:700;display:flex;align-items:center;justify-content:center;letter-spacing:.1px}
  .button--social{background:var(--social);font-size:5px}

  .options{position:absolute;left:19px;width:96px;display:flex;justify-content:space-between;align-items:center;font-size:4.6px;color:var(--ink)}
  .options__remember{display:flex;align-items:center;gap:3px}
  .tick-box{width:5px;height:5px;background:var(--white);display:flex;align-items:center;justify-content:center}
  .tick-box svg{width:4px;height:4px}

  .register-here{position:absolute;left:0;width:131px;text-align:center;font-size:4.6px;color:var(--ink);letter-spacing:.1px}
  .divider{position:absolute;left:9px;width:113px;display:flex;align-items:center;gap:6px;font-size:5.2px;color:var(--ink)}
  .divider::before,.divider::after{content:"";flex:1;height:.5px;background:#cfcfcf}
</style>
</head>
<body>

<svg width="0" height="0" style="position:absolute">
  <defs>
    <symbol id="icon-user" viewBox="0 0 10 10"><circle cx="5" cy="5" r="4.3" fill="none" stroke="#555" stroke-width="1"/><circle cx="5" cy="4" r="1.6" fill="#555"/><path d="M2.3 8a3 3 0 0 1 5.4 0" fill="#555"/></symbol>
    <symbol id="icon-lock" viewBox="0 0 10 10"><rect x="2" y="4.5" width="6" height="5" fill="#555"/><path d="M3.3 4.5V3a1.7 1.7 0 0 1 3.4 0v1.5" fill="none" stroke="#555" stroke-width="1"/></symbol>
    <symbol id="icon-mail" viewBox="0 0 10 10"><rect x="1" y="2" width="8" height="6" fill="none" stroke="#555" stroke-width="1"/><path d="M1 2.5l4 3 4-3" fill="none" stroke="#555" stroke-width="1"/></symbol>
    <symbol id="icon-pin" viewBox="0 0 10 10"><path d="M5 9.5S1.8 5.8 1.8 3.8a3.2 3.2 0 0 1 6.4 0C8.2 5.8 5 9.5 5 9.5z" fill="#555"/><circle cx="5" cy="3.8" r="1.1" fill="#fff"/></symbol>
    <symbol id="icon-tick" viewBox="0 0 10 10"><path d="M1.5 5.2l2.3 2.3L8.5 2.8" fill="none" stroke="#555" stroke-width="1.6"/></symbol>
    <linearGradient id="cafe-scene" x1="0" y1="0" x2="0" y2="1"><stop offset="0" stop-color="#e9a443"/><stop offset=".45" stop-color="#7d8a3a"/><stop offset="1" stop-color="#6b4a2c"/></linearGradient>
    <linearGradient id="soup-scene" x1="0" y1="0" x2="1" y2="1"><stop offset="0" stop-color="#fba437"/><stop offset="1" stop-color="#f58a1f"/></linearGradient>
    <linearGradient id="tomato-scene" x1="0" y1="0" x2="1" y2="1"><stop offset="0" stop-color="#f5f1ec"/><stop offset=".55" stop-color="#e85a3a"/><stop offset="1" stop-color="#b8322a"/></linearGradient>
    <linearGradient id="coffee-scene" x1="0" y1="0" x2="1" y2="0"><stop offset="0" stop-color="#5a3b26"/><stop offset=".5" stop-color="#b49a84"/><stop offset="1" stop-color="#d9cfc6"/></linearGradient>
    <linearGradient id="veg-scene" x1="0" y1="0" x2="1" y2="0"><stop offset="0" stop-color="#b9a05a"/><stop offset=".5" stop-color="#eadfc6"/><stop offset="1" stop-color="#9aab4e"/></linearGradient>
  </defs>
</svg>

<!-- Splash, light -->
<section class="screen screen--splash-light">
  <svg class="photo-top" style="height:60px" viewBox="0 0 131 60" role="img" aria-label="Wooden spoon and fresh celery at the top corners">
    <ellipse cx="35" cy="28" rx="18" ry="9" fill="#d7cfc6"/><ellipse cx="112" cy="22" rx="20" ry="16" fill="#9dc07a"/>
  </svg>
  <div class="brand-badge"><span class="brand-badge__name">Pebble<br>and<br>Pine</span></div>
  <svg class="photo-bottom" height="40" viewBox="0 0 131 40" role="img" aria-label="Carrot, spring onions and mushrooms along the bottom edge">
    <ellipse cx="38" cy="34" rx="34" ry="10" fill="#e9a15a"/><ellipse cx="108" cy="32" rx="26" ry="12" fill="#d9cbbb"/>
  </svg>
</section>

<!-- Splash, yellow -->
<section class="screen screen--splash-yellow" role="img" aria-label="Soft yellow food photograph behind the brand badge">
  <div class="brand-badge"><span class="brand-badge__name">Pebble<br>and<br>Pine</span></div>
</section>

<!-- Cafe registration, light -->
<section class="screen screen--cafe-light">
  <svg class="photo-top" viewBox="0 0 131 92" role="img" aria-label="Tea plantation at sunrise with a coffee cup and beans">
    <path d="M0 0H131V72C118 58 104 52 88 58 70 66 56 84 36 82 20 80 10 84 0 90Z" fill="url(#cafe-scene)"/>
  </svg>
  <div class="mini-badge"><span class="mini-badge__name">Pebble<br>and Pine</span></div>
  <h1 class="title">CAFE REGISTRATION</h1>
  <div class="field" style="top:114px">User Name<svg><use href="#icon-user"/></svg></div>
  <div class="field" style="top:132px">Password<svg><use href="#icon-lock"/></svg></div>
  <div class="field" style="top:150px">Email Address<svg><use href="#icon-mail"/></svg></div>
  <div class="field field--tall" style="top:169px">Address<svg><use href="#icon-pin"/></svg></div>
  <div class="button" style="top:199px">CAFE REGISTERATION</div>
  <div class="options" style="top:221px"><span class="options__remember"><span class="tick-box"><svg><use href="#icon-tick"/></svg></span>Remember Me</span><span>Forgot Password ?</span></div>
  <svg class="photo-bottom" height="47" viewBox="0 0 131 47" role="img" aria-label="Cup of black coffee with scattered coffee beans">
    <rect width="131" height="47" fill="url(#coffee-scene)" opacity=".55"/>
  </svg>
</section>

<!-- Cafe registration, yellow -->
<section class="screen screen--cafe-yellow">
  <svg class="photo-top" viewBox="0 0 131 92" role="img" aria-label="Tea plantation at sunrise with a coffee cup and beans">
    <path d="M0 0H131V72C118 58 104 52 88 58 70 66 56 84 36 82 20 80 10 84 0 90Z" fill="url(#cafe-scene)"/>
  </svg>
  <div class="mini-badge"><span class="mini-badge__name">Pebble<br>and Pine</span></div>
  <h1 class="title title--light">CAFE REGISTRATION</h1>
  <div class="field" style="top:114px">User Name<svg><use href="#icon-user"/></svg></div>
  <div class="field" style="top:132px">Password<svg><use href="#icon-lock"/></svg></div>
  <div class="field" style="top:150px">Email Address<svg><use href="#icon-mail"/></svg></div>
  <div class="field field--tall" style="top:169px">Address<svg><use href="#icon-pin"/></svg></div>
  <div class="button" style="top:199px">CAFE REGISTERATION</div>
  <div class="options" style="top:221px"><span class="options__remember"><span class="tick-box"><svg><use href="#icon-tick"/></svg></span>Remember Me</span><span>Forgot Password ?</span></div>
  <svg class="photo-bottom" height="47" viewBox="0 0 131 47" role="img" aria-label="Cup of black coffee with scattered coffee beans">
    <rect width="131" height="47" fill="url(#coffee-scene)" opacity=".45"/>
  </svg>
</section>

<!-- User registration, light -->
<section class="screen screen--user-light">
  <svg class="photo-top" viewBox="0 0 131 92" role="img" aria-label="Bowl of orange pumpkin soup on an orange backdrop">
    <path d="M0 0H131V80C118 90 104 74 88 72 68 70 52 82 30 80 16 79 8 74 0 76Z" fill="url(#soup-scene)"/>
  </svg>
  <div class="mini-badge"><span class="mini-badge__name">Pebble<br>and Pine</span></div>
  <h1 class="title">USER REGISTRATION</h1>
  <div class="field" style="top:114px;border:.5px solid #e6e6e6">User Name<svg><use href="#icon-user"/></svg></div>
  <div class="field" style="top:132px;border:.5px solid #e6e6e6">Password<svg><use href="#icon-lock"/></svg></div>
  <div class="button" style="top:150px">REGISTER NOW</div>
  <div class="options" style="top:174px"><span class="options__remember"><span class="tick-box"><svg><use href="#icon-tick"/></svg></span>Remember Me</span><span>Forgot Password ?</span></div>
  <div class="register-here" style="top:189px">REGISTER HERE</div>
  <div class="divider" style="top:202px">or</div>
  <div class="button button--social" style="top:214px">REGISTER WITH CHATTERLY</div>
  <svg class="photo-bottom" height="51" viewBox="0 0 131 51" role="img" aria-label="Onions and fresh vegetables along the bottom">
    <rect width="131" height="51" fill="url(#veg-scene)" opacity=".6"/>
  </svg>
</section>

<!-- User registration, yellow -->
<section class="screen screen--user-yellow">
  <svg class="photo-top" viewBox="0 0 131 92" role="img" aria-label="Pot of tomato soup with fresh tomatoes and basil">
    <path d="M0 0H131V84C118 92 104 78 86 74 66 70 52 60 30 66 16 70 8 72 0 74Z" fill="url(#tomato-scene)"/>
  </svg>
  <div class="mini-badge"><span class="mini-badge__name">Pebble<br>and Pine</span></div>
  <h1 class="title title--light">USER REGISTRATION</h1>
  <div class="field" style="top:114px">User Name<svg><use href="#icon-user"/></svg></div>
  <div class="field" style="top:132px">Password<svg><use href="#icon-lock"/></svg></div>
  <div class="button" style="top:150px">REGISTER NOW</div>
  <div class="options" style="top:174px"><span class="options__remember"><span class="tick-box"><svg><use href="#icon-tick"/></svg></span>Remember Me</span><span>Forgot Password ?</span></div>
  <div class="register-here" style="top:189px">REGISTER HERE</div>
  <div class="divider" style="top:202px">or</div>
  <div class="button button--social" style="top:214px">REGISTER WITH CHATTERLY</div>
  <svg class="photo-bottom" height="51" viewBox="0 0 131 51" role="img" aria-label="Onions and fresh vegetables along the bottom">
    <rect width="131" height="51" fill="url(#veg-scene)" opacity=".5"/>
  </svg>
</section>

</body>
</html>
```